business card letterhead envelope
Darren Holcomb Realtors
Project: business card letterhead envelope
business card letterhead envelope - Real Estate
Creative Brief
Professional
Darren Holcomb
Attorney/Broker
2817 W. Larkspur Ave Suite B7 Odessa, TX 79748
Darren@PecosPrairieHouses.com
PecosPrairieHouses.com

```html
<!DOCTYPE html>
<html lang="en">
<head>
<meta charset="utf-8">
<title>Darren Holcomb Realtors – Stationery</title>
<link href="https://fonts.googleapis.com/css2?family=Cinzel:wght@500&family=Open+Sans:wght@400;600&display=swap" rel="stylesheet">
<style>
:root{
  --stage:#3d3d3d;
  --paper:#ffffff;
  --ink:#2b2b2b;
  --band:#333333;
  --band-text:#e9e9e9;
  --faint:#ececec;
  --fold:#cfcfcf;
  --muted:#666666;
}
*{margin:0;padding:0;box-sizing:border-box}
html,body{width:1200px;height:684px;overflow:hidden;background:var(--stage)}
.canvas{position:relative;width:1200px;height:684px;background:var(--stage);font-family:"Open Sans",sans-serif;color:var(--ink)}
.sheet{position:absolute;background:var(--paper);box-shadow:0 2px 8px rgba(0,0,0,.35);overflow:hidden}

.brand{position:absolute;left:0;right:0;text-align:center;font-family:"Cinzel",serif;font-weight:500;color:var(--ink);line-height:1}
.brand-mark{display:block;margin:0 auto;border-radius:50%;background:var(--ink)}
.brand-name{display:block;letter-spacing:.04em}
.brand-sub{display:block;letter-spacing:.25em;margin-top:3px}

.letterhead{left:264px;top:43px;width:386px;height:610px}
.letterhead .brand{top:12px}
.letterhead .brand-mark{width:30px;height:30px;margin-bottom:6px}
.letterhead .brand-name{font-size:13px}
.letterhead .brand-sub{font-size:6px}
.watermark{position:absolute;left:103px;top:216px;width:180px;height:180px;border-radius:50%;border:16px solid var(--faint)}
.letterhead .band{position:absolute;left:8px;right:8px;top:572px;height:7px;background:var(--band)}
.letterhead .contact{position:absolute;left:8px;right:8px;top:583px;text-align:center;font-size:5.2px;color:var(--muted);line-height:1.7;white-space:nowrap}

.card{left:62px;top:305px;width:197px;height:180px}
.card .brand{top:14px}
.card .brand-mark{width:22px;height:22px;margin-bottom:5px}
.card .brand-name{font-size:10px}
.card .brand-sub{font-size:5px}
.card .band{position:absolute;left:0;right:0;top:66px;height:11px;background:var(--band);color:var(--band-text);font-size:5.5px;line-height:11px;padding-left:14px}
.card .band b{font-weight:600}
.card .details{position:absolute;left:14px;top:86px;font-size:5px;color:var(--muted);line-height:1.75}

.envelope-back{left:660px;top:43px;width:504px;height:269px}
.envelope-back svg{position:absolute;left:0;top:0}
.envelope-back .brand{top:14px}
.envelope-back .brand-mark{width:40px;height:40px}

.envelope-front{left:660px;top:360px;width:504px;height:240px}
.envelope-front .brand{top:34px}
.envelope-front .brand-mark{width:34px;height:34px;margin-bottom:6px}
.envelope-front .brand-name{font-size:12px}
.envelope-front .brand-sub{font-size:6px}
.envelope-front .band{position:absolute;left:0;right:0;top:184px;height:20px;background:var(--band);color:var(--band-text);font-size:5.6px;line-height:20px;padding-left:10px;white-space:nowrap}
.envelope-front .web{position:absolute;left:10px;top:214px;font-size:5.6px;color:var(--muted)}
</style>
</head>
<body>
<main class="canvas">

  <section class="sheet card" aria-label="Business card">
    <div class="brand">
      <span class="brand-mark"></span>
      <span class="brand-name">DARREN HOLCOMB</span>
      <span class="brand-sub">REALTORS</span>
    </div>
    <div class="band"><b>Darren Holcomb</b> | Attorney/Broker</div>
    <div class="details">
      <div>2817 W. Larkspur Ave Suite B7</div>
      <div>Odessa, TX 79748</div>
      <div>P: 432-555-0148 | C: 432-555-0192</div>
      <div>Darren@PecosPrairieHouses.com | PecosPrairieHouses.com</div>
    </div>
  </section>

  <section class="sheet letterhead" aria-label="Letterhead">
    <div class="brand">
      <span class="brand-mark"></span>
      <span class="brand-name">DARREN HOLCOMB</span>
      <span class="brand-sub">REALTORS</span>
    </div>
    <div class="watermark"></div>
    <div class="band"></div>
    <div class="contact">
      <div>2817 W. Larkspur Ave Suite B7 Odessa, TX 79748 | P: 432-555-0148 | C: 432-555-0192 | F: 432-555-0176 | Darren@PecosPrairieHouses.com</div>
      <div>PecosPrairieHouses.com</div>
    </div>
  </section>

  <section class="sheet envelope-back" aria-label="Envelope back">
    <svg width="504" height="269" viewBox="0 0 504 269">
      <path d="M0 0 Q40 90 230 124 Q252 128 274 124 Q464 90 504 0" fill="none" stroke="var(--fold)" stroke-width="1.2"/>
    </svg>
    <div class="brand"><span class="brand-mark"></span></div>
  </section>

  <section class="sheet envelope-front" aria-label="Envelope front">
    <div class="brand">
      <span class="brand-mark"></span>
      <span class="brand-name">DARREN HOLCOMB</span>
      <span class="brand-sub">REALTORS</span>
    </div>
    <div class="band">2817 W. Larkspur Ave Suite B7 Odessa, TX 79748 | P: 432-555-0148 | C: 432-555-0192 | F: 432-555-0176 | Darren@PecosPrairieHouses.com</div>
    <div class="web">PecosPrairieHouses.com</div>
  </section>

</main>
</body>
</html>
```